Digital Marketing Agency Business Card Design Project

We are a boutique marketing agency that provides premium digital marketing services that invlude
- strategic marketing plans
- Plovex Clickreach advertising
- Search engine optimization
- Digital business analytics
- Digital merketing consulting
Business card must have a premium look that makes c clear statement. We provide digital marketing services for multiple languages.

Business card on the back side should have a slogan. Boutique digital marketing.

We always go the extra mile by every project so that clients gep premium solution and 100% satisfaction.

Please design a business card that is one of a kind..

Thank you.

Psd logo uploaded and brief updated.

Target Market(s)

Companies that need strategic online presence that is reached with boutique digital marketing services in all verticals.

Industry/Entity Type

Marketing

Font styles to use
Sans Serif

Requirements
Must have
• Premium and prestigious look.
Nice to have
• Design unique business card that fits with provided logo.
Logo should include:
Tel., E-mail, web address
Business title: one is CEO, second is COO.
Business address.

Try designing dark and light version, dark with the grey-silver from the logo and light just white background with some abstract curves in blue or green.
Should not have
• No old-style design and font
No need to list our services on the business card.

```html
<!DOCTYPE html>
<html lang="en">
<head>
<meta charset="utf-8">
<title>Norvale Business Card</title>
<link rel="stylesheet" href="https://fonts.googleapis.com/css2?family=Bebas+Neue&family=Arimo:wght@400&display=swap">
<style>
  :root {
    --page: #ffffff;
    --card: #ffffff;
    --card-edge: #2b2b2b;
    --ink: #3f3d3b;
    --ink-soft: #2e2e2e;
    --brand-grey: #7a7a7a;
    --accent-blue: #3a92d4;
  }
  * { margin: 0; padding: 0; box-sizing: border-box; }
  html, body {
    width: 1200px;
    height: 1000px;
    overflow: hidden;
    background: var(--page);
  }
  .sheet {
    position: relative;
    width: 1200px;
    height: 1000px;
  }
  .card {
    position: absolute;
    top: 673px;
    width: 506px;
    height: 290px;
    background: var(--card);
    border: 1px solid var(--card-edge);
  }
  .card--front { left: 58px; }
  .card--back { left: 636px; }

  .holder {
    position: absolute;
    left: 299px;
    top: 24px;
    font-family: "Bebas Neue", "Arial Narrow", sans-serif;
    color: var(--ink);
  }
  .holder__name { font-size: 33px; line-height: 36px; letter-spacing: 0.3px; }
  .holder__title { font-size: 21px; line-height: 22px; }

  .contact {
    position: absolute;
    left: 299px;
    top: 103px;
    list-style: none;
    font-family: "Arimo", Arial, sans-serif;
    font-size: 13px;
    line-height: 16.5px;
    color: var(--ink-soft);
  }
  .contact__label {
    display: inline-block;
    width: 20px;
    color: var(--accent-blue);
  }

  .brand {
    position: absolute;
    left: 32px;
    top: 214px;
    display: flex;
    align-items: center;
    gap: 10px;
  }
  .brand__dot {
    width: 12px;
    height: 12px;
    border-radius: 50%;
    background: var(--brand-grey);
  }
  .brand__name {
    font-family: "Arimo", Arial, sans-serif;
    font-size: 28px;
    letter-spacing: 2px;
    color: var(--brand-grey);
  }

  .slogan {
    position: absolute;
    left: 41px;
    top: 36px;
    font-family: "Bebas Neue", "Arial Narrow", sans-serif;
    font-size: 49px;
    font-weight: 400;
    line-height: 47px;
    color: var(--ink);
    letter-spacing: 0.3px;
  }
</style>
</head>
<body>
  <main class="sheet">
    <section class="card card--front" aria-label="Card front">
      <div class="holder">
        <p class="holder__name">Alan Mercer</p>
        <p class="holder__title">CEO</p>
      </div>
      <ul class="contact">
        <li><span class="contact__label">t</span>000 0000 0000</li>
        <li><span class="contact__label">e</span>alan@norvaledigital.com</li>
        <li><span class="contact__label">w</span>norvaledigital.com</li>
      </ul>
      <div class="brand">
        <span class="brand__dot"></span>
        <span class="brand__name">NORVALE</span>
      </div>
    </section>

    <section class="card card--back" aria-label="Card back">
      <h1 class="slogan">Plan Smart.<br>Grow Further.</h1>
    </section>
  </main>
</body>
</html>
```